Mobile Product Filter for Luxury footwear e-commerce store

We would like to see designs for a "Mobile First" product filter for our collection pages:
http://shop.quillarven.example/collections/mukluks

The design should have a high degree of mobile usability and fit with the current look & feel.

Filtering options would be:

- Category: Mukluks / Moccasins / Puddlestep / Accessories
- Size: 5,6,7,8,9,10,11,12,13
- Gender: Male / Female / Unisex / Kids
- Color: Ideally show color swatches otherwise color names (Tan / Stone / Black / Cocoa /Tobacco / Russet)
- Sole: Korlex / Crepe / Leather
- Materials: Fur / Faux Fur / No Fur
- Production: Made in Canada / International
- Price: Up to $100 / $100 to $500 / $500 and more
- In Stock: Yes / No

** Sorting Options**
- Most Popular
- Highest Rates
- Price: High to Low
- Price: Low to High

BONUS POINTS: Provide the desktop view as well.

Target Market(s)

Women

Industry/Entity Type

E-Commerce

Number of Pages Required

2 page

Font styles to use
Sans Serif

Requirements
Must have
• Mobile first design
Nice to have
• Desktop design

```html
<!DOCTYPE html>
<html lang="en">
<head>
<meta charset="utf-8">
<title>Quillarven – Product Filter</title>
<link href="https://fonts.googleapis.com/css2?family=Lato:wght@400;700;900&display=swap" rel="stylesheet">
<style>
  :root {
    --ink: #000000;
    --white: #ffffff;
    --accent: #d53a1d;
    --text: #333333;
    --muted: #8a8a8a;
    --line: #cfcfcf;
    --field: #f6f6f6;
    --bar: #f1f1f1;
    --dark: #222222;
    --battery: #7ed321;
    --tan: #c59b5c;
    --stone: #a8a8a8;
    --black: #000000;
    --cocoa: #6a1e1e;
    --tobacco: #6c5238;
    --russet: #a41b12;
  }
  * { box-sizing: border-box; margin: 0; padding: 0; }
  html, body { width: 1200px; height: 2272px; overflow: hidden; }
  body {
    position: relative;
    background: var(--white);
    font-family: "Lato", Arial, sans-serif;
    color: var(--text);
  }
  .abs { position: absolute; }

  /* status bar */
  .status-bar {
    left: 0; top: 0; width: 1200px; height: 48px;
    background: var(--ink); color: var(--white);
    font-size: 24px; line-height: 48px;
  }
  .status-bar .signal { left: 16px; top: 0; display: flex; gap: 6px; align-items: center; height: 48px; }
  .status-bar .dot { width: 14px; height: 14px; border-radius: 50%; background: var(--white); }
  .status-bar .dot.off { background: transparent; border: 2px solid var(--white); }
  .status-bar .carrier { left: 210px; top: 0; }
  .status-bar .clock { left: 0; width: 1200px; text-align: center; top: 0; }
  .status-bar .battery { right: 40px; top: 12px; width: 110px; height: 26px; border: 2px solid var(--white); border-radius: 4px; padding: 2px; }
  .status-bar .battery span { display: block; height: 100%; width: 100%; background: var(--battery); }
  .status-bar .battery-tip { right: 32px; top: 19px; width: 6px; height: 12px; background: var(--white); }

  /* header */
  .site-header { left: 0; top: 48px; width: 1200px; height: 240px; background: var(--ink); }
  .brand { left: 0; width: 1160px; top: 76px; display: flex; justify-content: center; align-items: center; gap: 18px;
    color: var(--white); font-weight: 900; font-size: 76px; letter-spacing: 4px; line-height: 1; }
  .brand-mark { width: 20px; height: 20px; border-radius: 50%; background: var(--white); }
  .menu-toggle { left: 976px; top: 82px; width: 100px; }
  .menu-toggle span { display: block; height: 10px; background: var(--white); margin-bottom: 12px; }

  /* filter bar */
  .filter-bar { left: 0; top: 288px; width: 1200px; height: 98px; background: var(--bar); border-bottom: 2px solid #e2e2e2; }
  .filter-bar .title { left: 120px; top: 26px; font-size: 40px; color: var(--text); }
  .filter-bar svg { left: 444px; top: 38px; }

  /* form */
  .label { color: var(--accent); font-size: 42px; }
  .select { height: 116px; border: 2px solid var(--line); background: var(--field); }
  .select .value { position: absolute; left: 34px; top: 0; line-height: 112px; font-size: 36px; color: var(--muted); }
  .select .arrow { position: absolute; right: 0; top: 0; width: 122px; height: 112px; border-left: 2px solid var(--line);
    display: flex; align-items: center; justify-content: center; }

  .sizes { left: 112px; top: 680px; width: 976px; height: 100px; display: grid; grid-template-columns: repeat(9, 1fr);
    border: 2px solid var(--line); background: var(--field); }
  .sizes span { border-left: 2px solid var(--line); text-align: center; line-height: 96px; font-size: 36px; color: var(--muted); }
  .sizes span:first-child { border-left: none; }

  .check { display: flex; align-items: center; gap: 18px; font-size: 34px; color: var(--muted); white-space: nowrap; }
  .check i { display: block; width: 56px; height: 56px; border: 2px solid var(--line); background: var(--field); border-radius: 4px; }

  .swatch { display: flex; align-items: center; gap: 12px; font-size: 30px; color: var(--muted); white-space: nowrap; }
  .swatch i { display: block; width: 48px; height: 40px; }

  .message-bar { left: 112px; top: 2152px; width: 976px; height: 120px; background: var(--dark); color: var(--white); font-size: 42px; }
  .message-bar .text { left: 72px; top: 0; line-height: 116px; }
  .message-bar svg { right: 60px; top: 40px; }
</style>
</head>
<body>

<div class="abs status-bar">
  <div class="abs signal"><i class="dot"></i><i class="dot"></i><i class="dot"></i><i class="dot"></i><i class="dot off"></i></div>
  <div class="abs carrier">Ferncell IN 3G</div>
  <div class="abs clock">9:52 am</div>
  <div class="abs battery"><span></span></div>
  <div class="abs battery-tip"></div>
</div>

<header class="abs site-header">
  <div class="abs brand"><span>QUILLARVEN</span><i class="brand-mark"></i></div>
  <div class="abs menu-toggle"><span></span><span></span><span></span></div>
</header>

<div class="abs filter-bar">
  <div class="abs title">Product by Filter</div>
  <svg class="abs" width="52" height="28" viewBox="0 0 52 28"><polyline points="3,3 26,24 49,3" fill="none" stroke="#888" stroke-width="3"/></svg>
</div>

<!-- Category -->
<div class="abs label" style="left:112px;top:400px;">Category</div>
<div class="abs select" style="left:112px;top:466px;width:976px;">
  <span class="value">Muluks</span>
  <span class="arrow"><svg width="52" height="28" viewBox="0 0 52 28"><polyline points="3,3 26,24 49,3" fill="none" stroke="#888" stroke-width="3"/></svg></span>
</div>

<!-- Size -->
<div class="abs label" style="left:112px;top:614px;">Size</div>
<div class="abs sizes">
  <span>05</span><span>06</span><span>07</span><span>08</span><span>09</span><span>10</span><span>11</span><span>12</span><span>13</span>
</div>

<!-- Gender -->
<div class="abs label" style="left:112px;top:842px;">Gender</div>
<label class="abs check" style="left:112px;top:916px;"><i></i>Male</label>
<label class="abs check" style="left:300px;top:916px;"><i></i>Female</label>
<label class="abs check" style="left:516px;top:916px;"><i></i>Unisex</label>
<label class="abs check" style="left:724px;top:916px;"><i></i>Kids</label>

<!-- Color -->
<div class="abs label" style="left:112px;top:1030px;">Color</div>
<div class="abs swatch" style="left:112px;top:1098px;"><i style="background:var(--tan)"></i>Tan</div>
<div class="abs swatch" style="left:250px;top:1098px;"><i style="background:var(--stone)"></i>Stone</div>
<div class="abs swatch" style="left:414px;top:1098px;"><i style="background:var(--black)"></i>Black</div>
<div class="abs swatch" style="left:576px;top:1098px;"><i style="background:var(--cocoa)"></i>Cocoa</div>
<div class="abs swatch" style="left:744px;top:1098px;"><i style="background:var(--tobacco)"></i>Tobacco</div>
<div class="abs swatch" style="left:936px;top:1098px;"><i style="background:var(--russet)"></i>Russet</div>

<!-- Sole / Materials -->
<div class="abs label" style="left:112px;top:1210px;">Sole</div>
<div class="abs select" style="left:112px;top:1276px;width:470px;">
  <span class="value">Korlex</span>
  <span class="arrow"><svg width="52" height="28" viewBox="0 0 52 28"><polyline points="3,3 26,24 49,3" fill="none" stroke="#888" stroke-width="3"/></svg></span>
</div>
<div class="abs label" style="left:618px;top:1210px;">Materials</div>
<div class="abs select" style="left:618px;top:1276px;width:470px;">
  <span class="value">Fur</span>
  <span class="arrow"><svg width="52" height="28" viewBox="0 0 52 28"><polyline points="3,3 26,24 49,3" fill="none" stroke="#888" stroke-width="3"/></svg></span>
</div>

<!-- Production -->
<div class="abs label" style="left:112px;top:1444px;">Production</div>
<div class="abs select" style="left:112px;top:1510px;width:976px;">
  <span class="value">Made in Canada</span>
  <span class="arrow"><svg width="52" height="28" viewBox="0 0 52 28"><polyline points="3,3 26,24 49,3" fill="none" stroke="#888" stroke-width="3"/></svg></span>
</div>

<!-- Price / In Stock -->
<div class="abs label" style="left:112px;top:1666px;">Price</div>
<div class="abs select" style="left:112px;top:1726px;width:470px;">
  <span class="value">Up to $100</span>
  <span class="arrow"><svg width="52" height="28" viewBox="0 0 52 28"><polyline points="3,3 26,24 49,3" fill="none" stroke="#888" stroke-width="3"/></svg></span>
</div>
<div class="abs label" style="left:618px;top:1666px;">In Stock</div>
<div class="abs select" style="left:618px;top:1726px;width:470px;">
  <span class="value">Yes</span>
  <span class="arrow"><svg width="52" height="28" viewBox="0 0 52 28"><polyline points="3,3 26,24 49,3" fill="none" stroke="#888" stroke-width="3"/></svg></span>
</div>

<!-- Sorting -->
<div class="abs label" style="left:112px;top:1906px;">Sorting Options</div>
<div class="abs select" style="left:112px;top:1984px;width:976px;">
  <span class="value">Most Popular</span>
  <span class="arrow"><svg width="52" height="28" viewBox="0 0 52 28"><polyline points="3,3 26,24 49,3" fill="none" stroke="#888" stroke-width="3"/></svg></span>
</div>

<!-- Message bar -->
<div class="abs message-bar">
  <div class="abs text">Leave a Message</div>
  <svg class="abs" width="60" height="36" viewBox="0 0 60 36"><polyline points="4,32 30,6 56,32" fill="none" stroke="#fff" stroke-width="7"/></svg>
</div>

</body>
</html>
```